Start-up Cleaning Business Needs Professional Business Cards

Marta's Butler Cleaning, LLC, is a start-up business based in the Northern Virginia suburbs of Washington, DC. MBC provides cleaning and housekeeping services for homes and offices. We have three core values:

1. We are personal. We value knowing and being known by our customers and each other. If you want nameless, faceless service, you should choose another provider. We put "personal" at the front of the list, because it is most important to us; the design we choose will convey this value.

2. Like a hotel concierge, we are professional in attitude, posture, communication and processes.

3. Like a hotel concierge, we solve problems with a can-do attitude and never make excuses.

Our uniforms are khaki pants with pink polo shirts.

Our logo is attached. There are other symbols, not represented in our logo, that may convey our values well, such as a top hat and bow tie, magnifying glass, desk bell, etc.

Please include fields for an individual's name and title, office phone number, mobile phone number, email address and website address (www.martasbutlercleaning.example).

Standard U.S. size: 2" x 3.5"
Updates

I should have mentioned that the purpose of all our advertising - business cards included - is to motivate potential customers to call or email to arrange a free in-home estimate.

```html
<!DOCTYPE html>
<html lang="en">
<head>
<meta charset="utf-8">
<title>Marta's Butler Cleaning — Business Card</title>
<link rel="stylesheet" href="https://fonts.googleapis.com/css2?family=Orbitron:wght@600&family=Nunito+Sans:wght@300;400&display=swap">
<style>
  :root {
    --backdrop: #bfbfbf;
    --card: #ffffff;
    --sky: #87d3f2;
    --sky-faint: #d6edf9;
    --ink: #333333;
  }
  html, body {
    margin: 0;
    padding: 0;
    width: 1200px;
    height: 1000px;
    overflow: hidden;
    background: var(--backdrop);
  }
  .stage {
    position: relative;
    width: 1200px;
    height: 1000px;
  }
  .card {
    position: absolute;
    background: var(--card);
  }
  .card--front {
    left: 123px;
    top: 302px;
    width: 544px;
    height: 319px;
    box-shadow: -3px 3px 4px rgba(0,0,0,0.55);
  }
  .front__band {
    position: absolute;
    left: 0; top: 0;
    width: 100%;
    height: 116px;
    background: var(--sky);
    text-align: center;
    color: var(--ink);
  }
  .front__name {
    margin: 0;
    padding-top: 42px;
    font-family: "Orbitron", sans-serif;
    font-size: 23px;
    line-height: 26px;
    letter-spacing: 1px;
    font-weight: 600;
  }
  .front__title {
    margin: 0;
    font-family: "Nunito Sans", sans-serif;
    font-size: 15px;
    line-height: 18px;
  }
  .front__emblem {
    position: absolute;
    left: 37px;
    top: 126px;
    width: 196px;
    height: 172px;
  }
  .contact {
    position: absolute;
    left: 245px;
    top: 183px;
    margin: 0;
    padding: 0;
    list-style: none;
    font-family: "Nunito Sans", sans-serif;
    font-size: 15px;
    color: var(--ink);
    line-height: 17px;
  }
  .contact__item {
    position: relative;
    padding-left: 21px;
    margin-bottom: 4px;
    white-space: nowrap;
  }
  .contact__item:nth-child(3),
  .contact__item:nth-child(4) { margin-top: 6px; }
  .contact__icon {
    position: absolute;
    left: 0;
    top: 2px;
    width: 13px;
    height: 13px;
  }
  .card--back {
    left: 769px;
    top: 153px;
    width: 318px;
    height: 543px;
  }
  .back__illustration {
    position: absolute;
    left: 46px;
    top: 50px;
    width: 216px;
    height: 346px;
  }
  .brand {
    position: absolute;
    left: 0;
    top: 395px;
    width: 100%;
    text-align: center;
    font-family: "Nunito Sans", sans-serif;
    font-weight: 300;
    color: var(--ink);
  }
  .brand__name {
    margin: 0;
    font-size: 62px;
    line-height: 76px;
  }
  .brand__tagline {
    margin: 0;
    font-size: 20px;
    letter-spacing: 2px;
    line-height: 24px;
  }
</style>
</head>
<body>
<main class="stage">
  <section class="card card--front">
    <header class="front__band">
      <h1 class="front__name">Quentin Moss</h1>
      <p class="front__title">CEO / Founder</p>
    </header>

    <svg class="front__emblem" role="img" aria-label="Faint illustration of a top hat, bow tie and magnifying glass" viewBox="0 0 196 172">
      <defs>
        <radialGradient id="emblemFade" cx="50%" cy="45%" r="60%">
          <stop offset="0%" stop-color="#d6edf9"/>
          <stop offset="100%" stop-color="#e6f4fb"/>
        </radialGradient>
      </defs>
      <rect x="0" y="0" width="196" height="172" rx="24" fill="url(#emblemFade)"/>
    </svg>

    <ul class="contact">
      <li class="contact__item">
        <svg class="contact__icon" viewBox="0 0 13 13" aria-hidden="true">
          <rect width="13" height="13" rx="2" fill="var(--sky)"/>
          <path d="M4 3 L5.5 3 L6 5 L5 6 Q6 8 7.5 8.5 L8.5 7.5 L10 8 L10 9.5 Q6 10 3.5 5 Z" fill="#fff"/>
        </svg>+1 555.010.2468
      </li>
      <li class="contact__item">
        <svg class="contact__icon" viewBox="0 0 13 13" aria-hidden="true">
          <rect width="13" height="13" rx="2" fill="var(--sky)"/>
          <rect x="3" y="4" width="7" height="5" fill="#fff"/>
          <path d="M3 4 L6.5 7 L10 4" stroke="var(--sky)" stroke-width="0.8" fill="none"/>
        </svg>quentin@mbc.example
      </li>
      <li class="contact__item">
        <svg class="contact__icon" viewBox="0 0 13 13" aria-hidden="true">
          <rect width="13" height="13" rx="2" fill="var(--sky)"/>
          <circle cx="6.5" cy="6.5" r="3.6" stroke="#fff" stroke-width="0.9" fill="none"/>
          <path d="M2.9 6.5 H10.1 M6.5 2.9 V10.1" stroke="#fff" stroke-width="0.8"/>
        </svg>www.martasbutlercleaning.example
      </li>
      <li class="contact__item">
        <svg class="contact__icon" viewBox="0 0 13 13" aria-hidden="true">
          <rect width="13" height="13" rx="2" fill="var(--sky)"/>
          <path d="M6.5 11 Q3.5 7.5 3.5 5.5 A3 3 0 0 1 9.5 5.5 Q9.5 7.5 6.5 11 Z" fill="#fff"/>
          <circle cx="6.5" cy="5.5" r="1.1" fill="var(--sky)"/>
        </svg>PO Box 000 0000 Maplecrest Lane<br>Hollowbrook VA 0000 USA
      </li>
    </ul>
  </section>

  <section class="card card--back">
    <svg class="back__illustration" role="img" aria-label="Sketched illustration of a housekeeper in a pink uniform mopping the floor" viewBox="0 0 216 346">
      <defs>
        <linearGradient id="figureTones" x1="0" y1="0" x2="0" y2="1">
          <stop offset="0%" stop-color="#f3e6e4"/>
          <stop offset="55%" stop-color="#f8dcea"/>
          <stop offset="100%" stop-color="#ece6e6"/>
        </linearGradient>
      </defs>
      <rect x="0" y="0" width="216" height="346" rx="18" fill="url(#figureTones)"/>
    </svg>

    <div class="brand">
      <p class="brand__name">Marta's</p>
      <p class="brand__tagline">Butler Cleaning</p>
    </div>
  </section>
</main>
</body>
</html>
```